ALL TEXT Social Media Graphics

We are looking for a series of social media graphics for Instagram (new size: 4:5 (1080 x 1350 pixels) ratio that are ALL TEXT. We want the following quotes below on each graphic; one quote per graphic. AND, In very small letters at the bottom of each graphic, add @PaulaWrenLive
The look and feel of these graphics should be complimentary to the color palette attached below; but keep them simple. But the design is up to you; at the end of this document, I provided various samples of all text graphics that I like as examples.
The Quotes are in the attached WORD document
women trying to lose weight

```html
<!DOCTYPE html>
<html lang="en">
<head>
<meta charset="utf-8">
<title>Sunkissed Reset Plan Quote Graphics</title>
<link href="https://fonts.googleapis.com/css2?family=Oswald:wght@500;600;700&display=swap" rel="stylesheet">
<style>
  :root {
    --backdrop: #4d4d4d;
    --card: #ffffff;
    --ink: #111111;
    --accent: #b0155a;
  }
  * { box-sizing: border-box; margin: 0; padding: 0; }
  html, body {
    width: 1200px; height: 813px; overflow: hidden;
    background: var(--backdrop);
  }
  .board { position: relative; width: 1200px; height: 813px; }
  .post {
    position: absolute;
    width: 216px; height: 269px;
    background: var(--card);
    padding: 43px 0 0 24px;
    font-family: "Oswald", "Arial Narrow", sans-serif;
    text-transform: uppercase;
    white-space: nowrap;
  }
  .row-1 { top: 101px; }
  .row-2 { top: 398px; }
  .col-1 { left: 46px; }
  .col-2 { left: 274px; }
  .col-3 { left: 497px; }
  .col-4 { left: 723px; }
  .col-5 { left: 950px; }
  .hook {
    color: var(--ink);
    font-weight: 600;
    font-size: 16.5px;
    line-height: 19px;
    letter-spacing: 0.1px;
  }
  .promise {
    margin-top: 19px;
    color: var(--accent);
    font-weight: 700;
    font-size: 19px;
    line-height: 20.5px;
  }
  .cta {
    margin-top: 3px;
    color: var(--ink);
    font-weight: 600;
    font-size: 8.5px;
    line-height: 12px;
  }
  .cta .keyword { color: var(--accent); }
  .handle {
    position: absolute;
    left: 24px; bottom: 31px;
    color: var(--ink);
    font-weight: 600;
    font-size: 6.5px;
    letter-spacing: 0.1px;
  }
</style>
</head>
<body>
<main class="board">

  <article class="post row-1 col-1">
    <p class="hook">You can absolutely be<br>down 20–30 pounds by<br>end of summer.</p>
    <p class="promise">All it takes is the<br>right plan and<br>you’ve found it.</p>
    <p class="cta">Comment <span class="keyword">“Sunkissed”</span> for the<br>Sunkissed Reset Plan!</p>
    <p class="handle">@PaulaWrenLive</p>
  </article>

  <article class="post row-1 col-2">
    <p class="hook">You don’t need<br>another diet you need<br>a system that works.</p>
    <p class="promise">Drop 30 pounds<br>with the Sunkissed<br>Reset Plan.</p>
    <p class="cta">Comment <span class="keyword">“Summer”</span> to start now!</p>
    <p class="handle">@PaulaWrenLive</p>
  </article>

  <article class="post row-1 col-3">
    <p class="hook">This summer ain’t<br>over and neither are<br>your body goals.</p>
    <p class="promise">Drop 30 pounds<br>with the Sunkissed<br>Reset Plan.</p>
    <p class="cta">Comment <span class="keyword">“Sunkissed”</span> to get the plan!</p>
    <p class="handle">@PaulaWrenLive</p>
  </article>

  <article class="post row-1 col-4">
    <p class="hook">If your goal is a tiny<br>waist, flat belly, and<br>30 pounds down</p>
    <p class="promise">This is the plan.</p>
    <p class="cta">Comment <span class="keyword">“Summer”</span> to join<br>the Sunkissed Reset Plan!!</p>
    <p class="handle">@PaulaWrenLive</p>
  </article>

  <article class="post row-1 col-5">
    <p class="hook">There’s still time to<br>drop the 30 pounds<br>and slay this summer.</p>
    <p class="promise">The Sunkissed<br>Reset Plan<br>has the blueprint.</p>
    <p class="cta">Comment <span class="keyword">“Sunkissed”</span>!</p>
    <p class="handle">@PaulaWrenLive</p>
  </article>

  <article class="post row-2 col-1">
    <p class="hook">Snatched waist, flat<br>tummy, 30 pounds<br>lighter</p>
    <p class="promise">That’s what the<br>Sunkissed Reset<br>Plan challenge<br>delivers.</p>
    <p class="cta">Comment <span class="keyword">“Sunkissed”</span> to get the plan</p>
    <p class="handle">@PaulaWrenLive</p>
  </article>

  <article class="post row-2 col-2">
    <p class="hook">Nothing feels better<br>than seeing that scale<br>drop week after week.</p>
    <p class="promise">Let’s lose up to<br>30 pounds this<br>summer together.</p>
    <p class="cta">Comment <span class="keyword">“Summer”</span> to join<br>the Sunkissed Reset Plan!!</p>
    <p class="handle">@PaulaWrenLive</p>
  </article>

  <article class="post row-2 col-3">
    <p class="hook">Sis, we’re dropping<br>belly flat and saying<br>goodbye to stubborn<br>pounds.</p>
    <p class="promise">Join the Sunkissed<br>Reset Plan.</p>
    <p class="cta">Comment <span class="keyword">“Summer”</span>!</p>
    <p class="handle">@PaulaWrenLive</p>
  </article>

  <article class="post row-2 col-4">
    <p class="hook">Don’t wait ‘til next<br>summer to get right.<br>The time is now.</p>
    <p class="promise">Drop 30 pounds<br>with the Sunkissed<br>Reset Plan.</p>
    <p class="cta">Comment <span class="keyword">“Summer”</span>!</p>
    <p class="handle">@PaulaWrenLive</p>
  </article>

  <article class="post row-2 col-5">
    <p class="hook">You’ve got 8 weeks and<br>the perfect plan to<br>drop 30 pounds.</p>
    <p class="promise">Let’s get snatched<br>this summer with<br>the Sunkissed<br>Reset Plan.</p>
    <p class="cta">Comment <span class="keyword">“Summer”</span>!</p>
    <p class="handle">@PaulaWrenLive</p>
  </article>

</main>
</body>
</html>
```